Artistically challenged consultant needs a sexy business card.

I need a business card design for my consultancy business. I work primarily in the pacific on international development program focusing on tourism, economic empowerment and training. I would like to use a light blue/green to reference the pacific and also a simple design of a sprouting coconut (photo attached for reference) to reference growth and development.
The business card should have icons for email, phone, skype, ABN and linked in.

```html
<!DOCTYPE html>
<html lang="en">
<head>
<meta charset="utf-8">
<title>Mara Ellison Consulting – Business Card</title>
<link rel="stylesheet" href="https://fonts.googleapis.com/css2?family=Open+Sans:wght@400;500&display=swap">
<style>
  :root {
    --backdrop: #e6e7e9;
    --card: #ffffff;
    --ink: #5b5b5b;
    --ink-soft: #4a4a4a;
    --icon: #6a6a6a;
    --placeholder: #eeedea;
  }
  * { margin: 0; padding: 0; box-sizing: border-box; }
  html, body {
    width: 1200px;
    height: 693px;
    overflow: hidden;
    background: var(--backdrop);
    font-family: "Open Sans", Arial, sans-serif;
  }
  .business-card {
    position: absolute;
    left: 150px;
    top: 91px;
    width: 900px;
    height: 510px;
    background: var(--card);
    border-radius: 24px;
    box-shadow: 0 2px 10px rgba(0, 0, 0, 0.12);
  }
  .illustration-area {
    position: absolute;
    left: 120px;
    top: 126px;
    width: 153px;
    height: 255px;
    background: var(--placeholder);
    border-radius: 4px;
  }
  .company-name {
    position: absolute;
    right: 63px;
    top: 118px;
    font-size: 36px;
    font-weight: 400;
    color: var(--ink);
    letter-spacing: 0.2px;
    white-space: nowrap;
  }
  .contact-list {
    position: absolute;
    right: 63px;
    top: 331px;
    list-style: none;
  }
  .contact-item {
    display: flex;
    justify-content: flex-end;
    align-items: center;
    height: 34px;
    font-size: 21px;
    font-weight: 500;
    color: var(--ink-soft);
    white-space: nowrap;
  }
  .contact-icon {
    width: 21px;
    height: 21px;
    margin-left: 15px;
    flex: none;
  }
  .contact-icon--plain {
    background: var(--icon);
    border-radius: 2px;
  }
</style>
</head>
<body>
  <main class="business-card">
    <div class="illustration-area" role="img" aria-label="Illustration of a sprouting coconut"></div>

    <h1 class="company-name">Mara Ellison Consulting</h1>

    <ul class="contact-list">
      <li class="contact-item">
        <span>+61 400 555 019</span>
        <svg class="contact-icon" viewBox="0 0 20 20" aria-label="Phone">
          <rect width="20" height="20" rx="2" fill="var(--icon)"/>
          <path d="M6 4.5c.6-.4 1.3-.2 1.6.4l.9 1.8c.2.5.1 1-.3 1.3l-.8.6c.6 1.4 1.6 2.4 3 3l.6-.8c.3-.4.8-.5 1.3-.3l1.8.9c.6.3.8 1 .4 1.6l-.7 1c-.5.6-1.3.9-2.1.6-3.2-1.1-5.6-3.5-6.7-6.7-.3-.8 0-1.6.6-2.1z" fill="#ffffff"/>
        </svg>
      </li>
      <li class="contact-item">
        <span>mara ellison</span>
        <span class="contact-icon contact-icon--plain" aria-label="Chat"></span>
      </li>
      <li class="contact-item">
        <span>mara ellison</span>
        <span class="contact-icon contact-icon--plain" aria-label="Professional network"></span>
      </li>
      <li class="contact-item">
        <span>me@maraellisonconsulting.com</span>
        <svg class="contact-icon" viewBox="0 0 20 20" aria-label="Email">
          <rect width="20" height="20" rx="2" fill="var(--icon)"/>
          <rect x="4" y="6" width="12" height="8.5" rx="0.8" fill="#ffffff"/>
          <path d="M4.5 6.5l5.5 4.2 5.5-4.2" fill="none" stroke="var(--icon)" stroke-width="1.2"/>
        </svg>
      </li>
    </ul>
  </main>
</body>
</html>
```